Harborline Security and Surveillance Business Card

Business Card Design - Company Name:Freedom Security and SurveillanceWe are a Security Systems Integrator Specializing in Security Systems/ Video Surveillance and Access Control. Our areas of expertise are:Security SystemsVideo SurveillanceAccess ControlFire Alarm SystemsNetwork CablingCellular BoostersMy input is the Front of the Card is: logo, name of Business, My Name, Phone Number, and email.Rear of Card is the 6 areas of expertise, I just dont want the front to be very busy.
Name: Tom Werner
Title: President
Email: tom@harborlinesecsys.example
website: harborlinesecsys.example

```html
<!DOCTYPE html>
<html lang="en">
<head>
<meta charset="utf-8">
<title>Harborline Security and Surveillance – Business Card</title>
<link rel="stylesheet" href="https://fonts.googleapis.com/css2?family=Ubuntu:wght@400;500;700&display=swap">
<style>
  :root {
    --page: #ececec;
    --card: #121212;
    --blue: #2460b0;
    --silver: #c4c6c9;
    --silver-dark: #8d9094;
    --white: #f4f4f4;
  }
  * { box-sizing: border-box; margin: 0; padding: 0; }
  html, body {
    width: 1200px; height: 900px; overflow: hidden;
    background: var(--page);
    font-family: "Ubuntu", sans-serif;
  }
  .sheet {
    width: 1200px; height: 900px;
    display: flex; flex-direction: column; align-items: center; justify-content: center;
    gap: 40px;
  }
  .card {
    position: relative;
    width: 700px; height: 400px;
    background: var(--card);
    overflow: hidden;
    box-shadow: 0 6px 18px rgba(0,0,0,.18);
  }

  /* Contact side */
  .brand-line {
    position: absolute; left: 48px; top: 52px;
    display: flex; align-items: center; gap: 12px;
  }
  .brand-mark { width: 18px; height: 18px; background: var(--blue); }
  .brand-name {
    color: var(--blue); font-weight: 500; font-size: 17px;
    letter-spacing: 1.5px; text-transform: uppercase;
  }
  .person { position: absolute; left: 48px; top: 200px; }
  .person-name {
    color: var(--blue); font-weight: 500; font-size: 22px; text-transform: uppercase;
  }
  .person-title { color: var(--white); font-size: 18px; margin-top: 2px; }
  .contact-list { list-style: none; margin-top: 20px; }
  .contact-list li {
    display: flex; align-items: center; gap: 14px;
    color: var(--white); font-size: 18px; line-height: 30px;
  }
  .contact-list svg { width: 18px; height: 18px; fill: var(--blue); flex: none; }

  /* Services side */
  .brand-center {
    position: absolute; left: 0; right: 0; top: 120px;
    text-align: center;
  }
  .brand-center .brand-name { font-size: 30px; letter-spacing: 3px; }
  .brand-rule {
    width: 460px; height: 2px; margin: 14px auto 0;
    background: var(--silver-dark);
  }
  .swoosh { position: absolute; left: 0; bottom: 0; width: 700px; height: 170px; }
  .services {
    position: absolute; left: 0; right: 0; bottom: 34px;
    color: var(--white); font-size: 19px; line-height: 30px; text-align: center;
  }
  .services .dot { margin: 0 8px; }
</style>
</head>
<body>
<main class="sheet">

  <section class="card card-contact">
    <div class="brand-line">
      <span class="brand-mark"></span>
      <span class="brand-name">Harborline Security and Surveillance</span>
    </div>
    <div class="person">
      <p class="person-name">Tom Werner</p>
      <p class="person-title">President</p>
      <ul class="contact-list">
        <li>
          <svg viewBox="0 0 24 24" aria-hidden="true"><path d="M6.6 10.8a15 15 0 0 0 6.6 6.6l2.2-2.2c.3-.3.7-.4 1-.2 1.1.4 2.3.6 3.6.6.6 0 1 .4 1 1V20c0 .6-.4 1-1 1A17 17 0 0 1 3 4c0-.6.4-1 1-1h3.5c.6 0 1 .4 1 1 0 1.3.2 2.5.6 3.6.1.3 0 .7-.2 1z"/></svg>
          123 456 7890
        </li>
        <li>
          <svg viewBox="0 0 24 24" aria-hidden="true"><path d="M2 5h20v14H2z M3.5 6.5 12 13l8.5-6.5" stroke="#121212" stroke-width="1.6"/></svg>
          tom@harborlinesecsys.example
        </li>
        <li>
          <svg viewBox="0 0 24 24" aria-hidden="true"><circle cx="12" cy="12" r="10"/><path d="M2 12h20M12 2c3 3 3 17 0 20M12 2c-3 3-3 17 0 20" stroke="#121212" stroke-width="1.4" fill="none"/></svg>
          www.harborlinesecsys.example
        </li>
      </ul>
    </div>
  </section>

  <section class="card card-services">
    <div class="brand-center">
      <span class="brand-name">Harborline Security and Surveillance</span>
      <div class="brand-rule"></div>
    </div>
    <svg class="swoosh" viewBox="0 0 700 170" preserveAspectRatio="none" aria-hidden="true">
      <defs>
        <linearGradient id="silverBand" x1="0" x2="1">
          <stop offset="0" stop-color="#7d8084"/>
          <stop offset=".5" stop-color="#e4e5e7"/>
          <stop offset="1" stop-color="#9a9da1"/>
        </linearGradient>
      </defs>
      <path d="M0 30 Q350 -10 700 22 L700 170 L0 170 Z" fill="url(#silverBand)"/>
      <path d="M0 62 Q350 18 700 40 L700 170 L0 170 Z" fill="#2460b0"/>
    </svg>
    <p class="services">
      Security Systems<span class="dot">•</span>Video Surveillance<span class="dot">•</span>Access Control<br>
      Fire Alarm Systems<span class="dot">•</span>Network Cabling<span class="dot">•</span>Cellular Boosters
    </p>
  </section>

</main>
</body>
</html>
```